7 P's for Healthcare Companies - Textbook Graphic

Can you create a graphic for me for a medical textbook? The goal is to show 7 critical features of a healthcare startup and the audience is physicians with limited business backgrounds.

Please include a picture of young, male emergency physician in the middle of the graphic. Show them evaluating an idea. Can you surround the physician with bold writing for the seven components, and use brief descriptions and simple images or graphics to illustrate the point?

The image should be somewhat formal, but it's OK to be lighthearded.

The seven P's and brief descriptions include the following:
Product: what is their market solution?
(Intellectual) Property: do they have a patent or trademark?
Product Clearance: how will they get KLN approval and TPR clearance?
Payment: how will they make money?
Pilots: have they applied their product in a healthcare setting?
Physician and Patient feedback: Do doctors and patients like their product?
Publication: do they have evidence their product works?

More detail and information is available at this website: https://quvenlo.com/blog/uncategorized/healthcare-framework/

I will need to own this image

```html
<!DOCTYPE html>
<html lang="en">
<head>
<meta charset="utf-8">
<title>7 P's for Healthcare Companies</title>
<link rel="stylesheet" href="https://fonts.googleapis.com/css2?family=Arimo:wght@400;700&family=Oswald:wght@600&display=swap">
<style>
  :root {
    --backdrop: #ababab;
    --paper: #ffffff;
    --header: #474645;
    --ink: #111111;
    --red: #c21f26;
    --orange: #f17f20;
    --green: #47883d;
    --sky: #35c5ef;
    --navy: #2f4ea1;
    --purple: #8160aa;
    --pink: #ef6aa9;
    --hub-ring: #454545;
  }
  * { margin: 0; padding: 0; box-sizing: border-box; }
  html, body { width: 1200px; height: 1200px; overflow: hidden; background: var(--backdrop); }
  .poster {
    position: absolute; left: 228px; top: 78px; width: 744px; height: 1043px;
    background: var(--paper);
  }
  .poster-header {
    height: 170px; background: var(--header); color: #fff; text-align: center;
    font-family: "Arimo", Arial, sans-serif; font-weight: 700;
  }
  .poster-title { font-size: 90px; line-height: 1; padding-top: 14px; letter-spacing: 1px; }
  .poster-subtitle { font-size: 46px; line-height: 1; margin-top: 2px; }
  .wheel { display: block; width: 744px; height: 873px; }
  .label { font-family: "Oswald", "Arial Narrow", sans-serif; font-weight: 600; font-size: 31px; fill: var(--ink); text-anchor: middle; }
  .desc { font-family: "Arimo", Arial, sans-serif; font-size: 23.5px; fill: var(--ink); text-anchor: middle; }
  .ring { fill: none; stroke-width: 55; }
  .wedge { fill: none; stroke-width: 2.5; }
  .badge-outline { fill: #fff; stroke-width: 2.5; }
  .badge-shadow { fill: rgba(40,40,40,.45); }
  .badge-face { fill: #f7f7f7; }
</style>
</head>
<body>
<main class="poster">
  <header class="poster-header">
    <h1 class="poster-title">7 P's</h1>
    <p class="poster-subtitle">for Healthcare Companies</p>
  </header>

  <svg class="wheel" viewBox="368 400 1198 1406" xmlns="http://www.w3.org/2000/svg">
    <!-- ring segments -->
    <path class="ring" stroke="var(--orange)" d="M979.2 627.2 A453 453 0 0 1 1310.1 786.5"/>
    <path class="ring" stroke="var(--green)" d="M1327.8 808.8 A453 453 0 0 1 1409.6 1166.9"/>
    <path class="ring" stroke="var(--sky)" d="M1403.2 1194.7 A453 453 0 0 1 1174.2 1481.8"/>
    <path class="ring" stroke="var(--navy)" d="M1148.6 1494.1 A453 453 0 0 1 781.4 1494.1"/>
    <path class="ring" stroke="var(--purple)" d="M755.8 1481.8 A453 453 0 0 1 526.8 1194.7"/>
    <path class="ring" stroke="var(--pink)" d="M520.4 1166.9 A453 453 0 0 1 602.2 808.8"/>
    <path class="ring" stroke="var(--red)" d="M619.9 786.5 A453 453 0 0 1 950.8 627.2"/>

    <!-- wedge outlines -->
    <path class="wedge" stroke="var(--orange)" d="M978.4 653.2 L971.7 868.1 A212 212 0 0 1 1126.5 942.7 L1290.3 803.4"/>
    <path class="wedge" stroke="var(--green)" d="M1307 824.4 L1134.8 953.1 A212 212 0 0 1 1173.1 1120.7 L1384.1 1161.9"/>
    <path class="wedge" stroke="var(--sky)" d="M1378.1 1188.1 L1170.1 1133.7 A212 212 0 0 1 1062.9 1268 L1162.2 1458.7"/>
    <path class="wedge" stroke="var(--navy)" d="M1138.1 1470.3 L1050.9 1273.8 A212 212 0 0 1 879.1 1273.8 L791.9 1470.3"/>
    <path class="wedge" stroke="var(--purple)" d="M767.8 1458.7 L867.1 1268 A212 212 0 0 1 759.9 1133.7 L551.9 1188.1"/>
    <path class="wedge" stroke="var(--pink)" d="M545.9 1161.9 L756.9 1120.7 A212 212 0 0 1 795.2 953.1 L623 824.4"/>
    <path class="wedge" stroke="var(--red)" d="M639.7 803.4 L803.5 942.7 A212 212 0 0 1 958.3 868.1 L951.6 653.2"/>

    <!-- hub -->
    <defs>
      <radialGradient id="hubFill" cx="50%" cy="45%" r="60%">
        <stop offset="0" stop-color="#dedede"/>
        <stop offset="0.6" stop-color="#d6d6d6"/>
        <stop offset="1" stop-color="#8f95c4"/>
      </radialGradient>
    </defs>
    <circle cx="965" cy="1080" r="200" fill="url(#hubFill)" stroke="var(--hub-ring)" stroke-width="10"
            role="img" aria-label="Illustration of a young male emergency physician in blue scrubs with a stethoscope, holding a red first-aid kit and waving"/>

    <!-- badges -->
    <g transform="translate(755 648)">
      <circle class="badge-outline" r="82" stroke="var(--red)"/>
      <circle r="72" fill="var(--red)"/>
      <circle class="badge-shadow" r="43" cx="10" cy="10"/>
      <circle class="badge-face" r="43"/>
      <g fill="var(--red)">
        <rect x="-12" y="-26" width="30" height="40" rx="2" opacity=".6"/>
        <rect x="-20" y="-22" width="30" height="42" rx="2"/>
        <g stroke="#fff" stroke-width="2.5"><line x1="-15" y1="-13" x2="5" y2="-13"/><line x1="-15" y1="-5" x2="5" y2="-5"/><line x1="-15" y1="3" x2="5" y2="3"/><line x1="-15" y1="11" x2="5" y2="11"/></g>
      </g>
    </g>
    <g transform="translate(1175 648)">
      <circle class="badge-outline" r="82" stroke="var(--orange)"/>
      <circle r="72" fill="var(--orange)"/>
      <circle class="badge-shadow" r="43" cx="10" cy="10"/>
      <circle class="badge-face" r="43"/>
      <g fill="var(--orange)">
        <circle cy="-6" r="18"/>
        <rect x="-9" y="10" width="18" height="12" rx="3"/>
        <circle cy="-6" r="8" fill="none" stroke="#fff" stroke-width="4"/>
        <g stroke="var(--orange)" stroke-width="3" stroke-linecap="round"><line x1="-28" y1="-6" x2="-24" y2="-6"/><line x1="24" y1="-6" x2="28" y2="-6"/><line x1="-20" y1="-24" x2="-17" y2="-21"/><line x1="20" y1="-24" x2="17" y2="-21"/></g>
      </g>
    </g>
    <g transform="translate(1437 972)">
      <circle class="badge-outline" r="82" stroke="var(--green)"/>
      <circle r="72" fill="var(--green)"/>
      <circle class="badge-shadow" r="43" cx="10" cy="10"/>
      <circle class="badge-face" r="43"/>
      <g fill="var(--green)">
        <path d="M-10 8 L-12 28 L0 22 L12 28 L10 8 Z"/>
        <circle cy="-6" r="20"/>
        <circle cy="-6" r="13" fill="none" stroke="#fff" stroke-width="3"/>
        <path d="M5 -10 A7 7 0 1 0 5 -2" fill="none" stroke="#fff" stroke-width="3"/>
      </g>
    </g>
    <g transform="translate(1345 1383)">
      <circle class="badge-outline" r="82" stroke="var(--sky)"/>
      <circle r="72" fill="var(--sky)"/>
      <circle class="badge-shadow" r="43" cx="10" cy="10"/>
      <circle class="badge-face" r="43"/>
      <g fill="var(--sky)">
        <path d="M-12 -26 H10 L20 -16 V22 H-12 Z"/>
        <g stroke="#fff" stroke-width="2.5"><line x1="-2" y1="-8" x2="14" y2="-8"/><line x1="-2" y1="0" x2="14" y2="0"/><line x1="-2" y1="8" x2="14" y2="8"/></g>
        <circle cx="-14" cy="12" r="12" stroke="#fff" stroke-width="2"/>
        <path d="M-19 12 L-15 16 L-8 8" fill="none" stroke="#fff" stroke-width="2.5"/>
      </g>
    </g>
    <g transform="translate(966 1565)">
      <circle class="badge-outline" r="82" stroke="var(--navy)"/>
      <circle r="72" fill="var(--navy)"/>
      <circle class="badge-shadow" r="43" cx="10" cy="10"/>
      <circle class="badge-face" r="43"/>
      <g fill="var(--navy)">
        <rect x="-12" y="-24" width="34" height="20" rx="2" transform="rotate(12)"/>
        <circle cx="5" cy="-12" r="5" fill="#fff"/>
        <rect x="-28" y="4" width="8" height="20"/>
        <path d="M-18 6 H2 C8 6 8 12 2 12 H-6 L14 10 L26 2 C30 0 32 4 30 7 L16 20 H-18 Z"/>
      </g>
    </g>
    <g transform="translate(590 1388)">
      <circle class="badge-outline" r="82" stroke="var(--purple)"/>
      <circle r="72" fill="var(--purple)"/>
      <circle class="badge-shadow" r="43" cx="10" cy="10"/>
      <circle class="badge-face" r="43"/>
      <g fill="var(--purple)">
        <path d="M0 8 C-22 -6 -20 -24 -8 -24 C-4 -24 -1 -21 0 -18 C1 -21 4 -24 8 -24 C20 -24 22 -6 0 8 Z"/>
        <path d="M-3 -16 H3 V-12 H7 V-6 H3 V-2 H-3 V-6 H-7 V-12 H-3 Z" fill="#fff"/>
        <path d="M-28 -6 L-24 -6 L-20 10 L-4 18 L-4 26 L-14 26 L-28 10 Z"/>
        <path d="M28 -6 L24 -6 L20 10 L4 18 L4 26 L14 26 L28 10 Z"/>
      </g>
    </g>
    <g transform="translate(497 975)">
      <circle class="badge-outline" r="82" stroke="var(--pink)"/>
      <circle r="72" fill="var(--pink)"/>
      <circle class="badge-shadow" r="43" cx="10" cy="10"/>
      <circle class="badge-face" r="43"/>
      <g fill="none" stroke="var(--pink)" stroke-width="3.5" stroke-linecap="round">
        <path d="M-16 -28 V-18 A8 8 0 0 0 0 -18 V-28"/>
        <path d="M-8 -10 V-4"/>
        <circle cx="18" cy="-20" r="4"/>
        <path d="M18 -16 V-6"/>
      </g>
      <rect x="-28" y="-2" width="56" height="22" rx="3" fill="var(--pink)"/>
      <g fill="#fff" font-family="Arimo, Arial, sans-serif" font-size="16" text-anchor="middle"><text x="-14" y="15">★</text><text x="0" y="15">★</text><text x="14" y="15">★</text></g>
    </g>

    <!-- text -->
    <text class="label" x="825" y="776" textLength="135" lengthAdjust="spacingAndGlyphs">Publication:</text>
    <text class="desc" x="825" y="810">Do they have evidence</text>
    <text class="desc" x="825" y="839">their product works?</text>

    <text class="label" x="1106" y="776" textLength="96" lengthAdjust="spacingAndGlyphs">Product:</text>
    <text class="desc" x="1106" y="810">What is their</text>
    <text class="desc" x="1106" y="839">market solution?</text>

    <text class="label" x="1270" y="971" textLength="146" lengthAdjust="spacingAndGlyphs">(Intellectual)</text>
    <text class="label" x="1270" y="1004" textLength="104" lengthAdjust="spacingAndGlyphs">Property:</text>
    <text class="desc" x="1270" y="1038">Do they have a</text>
    <text class="desc" x="1270" y="1067">patent or</text>
    <text class="desc" x="1270" y="1096">trademark?</text>

    <text class="label" x="1200" y="1222" textLength="87" lengthAdjust="spacingAndGlyphs">Product</text>
    <text class="label" x="1200" y="1255" textLength="118" lengthAdjust="spacingAndGlyphs">Clearance:</text>
    <text class="desc" x="1200" y="1288">How will they get</text>
    <text class="desc" x="1200" y="1317">KLN approval</text>
    <text class="desc" x="1200" y="1347">and TPR</text>
    <text class="desc" x="1200" y="1376">clearance?</text>

    <text class="label" x="963" y="1362" textLength="104" lengthAdjust="spacingAndGlyphs">Payment:</text>
    <text class="desc" x="963" y="1402">How will they</text>
    <text class="desc" x="963" y="1431">make money?</text>

    <text class="label" x="731" y="1224" textLength="72" lengthAdjust="spacingAndGlyphs">Pilots:</text>
    <text class="desc" x="731" y="1262">Have they</text>
    <text class="desc" x="731" y="1291">applied their product</text>
    <text class="desc" x="731" y="1320">in a</text>
    <text class="desc" x="731" y="1349">healthcare</text>
    <text class="desc" x="731" y="1379">setting?</text>

    <text class="label" x="666" y="955" textLength="155" lengthAdjust="spacingAndGlyphs">Physician and</text>
    <text class="label" x="666" y="988" textLength="80" lengthAdjust="spacingAndGlyphs">Patient</text>
    <text class="label" x="666" y="1021" textLength="110" lengthAdjust="spacingAndGlyphs">feedback:</text>
    <text class="desc" x="666" y="1054">Do doctors and</text>
    <text class="desc" x="666" y="1083">patients like</text>
    <text class="desc" x="666" y="1113">their product?</text>
  </svg>
</main>
</body>
</html>
```